Out Door Living brochure

We need a Great looking brochure to feature the latest in out door living. Showcasing out doors is the new living space.

I'm enclosing our logo and a brochure we had done recently it didn't have enough impact. This one was a single fold you can also provide a tri fold if you see fit. We like the verbiage, but if you can spice it up we would love to see that. This brochure will be added to our sales packet.
Thank you!!!

Target Market(s)

Home owners

Industry/Entity Type

Construction Company

Logo Text

(See logo) Beautiful Homes Built to Last Introducing Outdoor living 2017

Font styles to use
Serif

Requirements
Must have
• Logo and
• Beautiful Homes Built to Last
• Introducing Outdoor living 2017
Nice to have
• Benefits of outdoor living
Should not have
• Bad photos if these don't work let me know we can get others to replace the sapce

```html
<!DOCTYPE html>
<html lang="en">
<head>
<meta charset="utf-8">
<title>Outdoor Living 2017 Brochure</title>
<link href="https://fonts.googleapis.com/css2?family=Arimo:ital,wght@0,400;0,700;1,400;1,700&display=swap" rel="stylesheet">
<style>
  :root {
    --sky: #5aaee3;
    --sky-light: #7cc3ef;
    --slate: #6a6d72;
    --slate-dark: #55585c;
    --ink: #1d1d1f;
    --paper: #ffffff;
    --mist: #eef0f2;
    --stage: #f4f5f6;
  }
  * { margin: 0; padding: 0; box-sizing: border-box; }
  html, body { width: 1200px; height: 1200px; overflow: hidden; }
  body {
    background: var(--stage);
    font-family: "Arimo", Arial, sans-serif;
    position: relative;
  }
  .brochure {
    position: absolute;
    left: 100px; top: 250px;
    width: 1000px; height: 700px;
    display: flex;
    box-shadow: 0 10px 30px rgba(0,0,0,0.12);
  }
  .panel {
    position: relative;
    width: 500px; height: 700px;
    background: var(--paper);
    overflow: hidden;
  }
  .panel svg.art { position: absolute; left: 0; top: 0; }

  /* Back panel */
  .back-headline {
    position: absolute; left: 40px; top: 34px; width: 420px;
    text-align: center; font-style: italic; font-size: 17px; line-height: 1.25;
  }
  .back-headline .accent { color: var(--sky); display: block; }
  .back-headline .plain { color: var(--ink); display: block; }
  .caption-bar {
    position: absolute; left: 30px; top: 352px; width: 440px; height: 36px;
    background: var(--slate);
    color: var(--paper); font-style: italic; font-size: 14px;
    display: flex; align-items: center; justify-content: center;
    box-shadow: 0 4px 6px rgba(0,0,0,0.18);
  }
  .brand {
    position: absolute;
    display: flex; flex-direction: column; align-items: center; gap: 10px;
  }
  .brand .mark { width: 56px; height: 56px; background: var(--sky); }
  .brand .name {
    font-size: 11px; letter-spacing: 1.5px; color: var(--slate);
    text-transform: uppercase; white-space: nowrap;
  }
  .brand-back { left: 50px; top: 520px; }
  .contact {
    position: absolute; left: 270px; top: 518px; width: 200px;
    text-align: right; font-style: italic; font-size: 13px; line-height: 1.35; color: var(--ink);
  }
  .contact .phone { color: var(--sky); font-size: 20px; margin-bottom: 4px; }

  /* Front panel */
  .cover-title {
    position: absolute; left: 50px; top: 452px;
    text-transform: uppercase; font-weight: 700;
  }
  .cover-title .line-one { font-size: 22px; color: var(--ink); letter-spacing: 1px; }
  .cover-title .line-two { font-size: 36px; color: var(--sky); letter-spacing: 1px; line-height: 1.05; }
  .cover-title .line-three {
    display: inline-block; background: var(--slate); color: var(--paper);
    font-size: 32px; letter-spacing: 2px; padding: 2px 10px 0; margin: 3px 0 4px;
  }
  .cover-title .line-four { font-size: 20px; color: var(--sky); letter-spacing: 2.5px; }
  .brand-front { right: 25px; top: 560px; }
  .brand-front .name { font-size: 10px; letter-spacing: 1px; }
</style>
</head>
<body>
  <div class="brochure">
    <section class="panel panel-back">
      <svg class="art" width="500" height="700" viewBox="0 0 500 700">
        <defs>
          <linearGradient id="pool-deck" x1="0" y1="0" x2="1" y2="1">
            <stop offset="0" stop-color="#a9cfe0"/>
            <stop offset="0.35" stop-color="#4fb7c9"/>
            <stop offset="0.7" stop-color="#7d8a92"/>
            <stop offset="1" stop-color="#a3a8ad"/>
          </linearGradient>
          <linearGradient id="lower-wash" x1="0" y1="0" x2="0" y2="1">
            <stop offset="0" stop-color="#ffffff"/>
            <stop offset="1" stop-color="#e6e8ea"/>
          </linearGradient>
          <linearGradient id="base-band" x1="0" y1="0" x2="0" y2="1">
            <stop offset="0" stop-color="#7a7d82"/>
            <stop offset="1" stop-color="#55585c"/>
          </linearGradient>
        </defs>
        <rect x="40" y="92" width="420" height="246" fill="var(--paper)" stroke="var(--sky)" stroke-width="4"/>
        <rect x="48" y="100" width="404" height="230" fill="url(#pool-deck)" role="img" aria-label="Photo of a rooftop deck with a plunge pool, built-in cushioned bench and a potted palm"/>
        <path d="M0,470 C120,430 260,440 500,470 V700 H0 Z" fill="url(#lower-wash)"/>
        <path d="M0,470 C120,430 260,440 500,470" fill="none" stroke="var(--sky)" stroke-width="5"/>
        <rect x="0" y="650" width="500" height="50" fill="url(#base-band)"/>
      </svg>
      <h2 class="back-headline">
        <span class="accent">Innovative ideas that help stretch out</span>
        <span class="plain">the seasons, making it comfy and cozy.</span>
      </h2>
      <p class="caption-bar">Enjoy your staycation in the comfort of your own back yard</p>
      <div class="brand brand-back">
        <span class="mark"></span>
        <span class="name">Harbor Crest Builders</span>
      </div>
      <address class="contact">
        <div class="phone">Call: 555-014-2290</div>
        <div>Email: hello@harborcrestmail.net</div>
        <div>www.harborcrestbuilders.com</div>
        <div>1480 Marlow Lane,</div>
        <div>Bayview, CA 94012</div>
      </address>
    </section>

    <section class="panel panel-front">
      <svg class="art" width="500" height="700" viewBox="0 0 500 700">
        <defs>
          <linearGradient id="outdoor-kitchen" x1="0" y1="0" x2="1" y2="1">
            <stop offset="0" stop-color="#b9c2c8"/>
            <stop offset="0.3" stop-color="#6e5d4e"/>
            <stop offset="0.6" stop-color="#8a8f8c"/>
            <stop offset="0.85" stop-color="#79c6d6"/>
            <stop offset="1" stop-color="#c9d8e0"/>
          </linearGradient>
          <linearGradient id="cover-blue" x1="0" y1="0" x2="1" y2="1">
            <stop offset="0" stop-color="var(--sky)"/>
            <stop offset="1" stop-color="var(--sky-light)"/>
          </linearGradient>
        </defs>
        <path d="M0,0 H500 V350 C470,430 380,450 280,432 C180,415 80,400 0,400 Z" fill="url(#cover-blue)"/>
        <path d="M40,40 H300 C420,40 455,190 430,270 C405,345 340,368 290,368 H40 Z" fill="var(--paper)"/>
        <path d="M50,50 H298 C405,50 440,190 418,266 C396,336 338,356 290,356 H50 Z" fill="url(#outdoor-kitchen)" role="img" aria-label="Photo of a covered outdoor kitchen bar with pale blue stools by the water"/>
        <rect x="0" y="660" width="500" height="40" fill="var(--sky)"/>
      </svg>
      <h1 class="cover-title">
        <div class="line-one">Beautiful Homes</div>
        <div class="line-two">Built to Last</div>
        <div class="line-three">Introducing</div>
        <div class="line-four">Outdoor Living 2017</div>
      </h1>
      <div class="brand brand-front">
        <span class="mark"></span>
        <span class="name">Harbor Crest Builders</span>
      </div>
    </section>
  </div>
</body>
</html>
```